Reiki business card

Please see uploaded files. There is a word document on there explaining what is required and what the other uploaded files are for. I am after a soft, relaxing, warm welcoming feel to the card. Thank you.

Industry/Entity Type

Business

```html
<!DOCTYPE html>
<html lang="en">
<head>
<meta charset="utf-8">
<title>Reiki for Kids &amp; Creatures – Business Card</title>
<link rel="stylesheet" href="https://fonts.googleapis.com/css2?family=Carlito:ital,wght@0,400;0,700;1,400&display=swap">
<style>
  :root {
    --page: #ffffff;
    --ink: #ffffff;
    --navy-deep: #222744;
    --navy: #2d4672;
    --steel: #5c84a8;
    --mist: #aac4d6;
    --lavender: #8b98c0;
    --emblem: rgba(255, 255, 255, 0.92);
  }
  * { box-sizing: border-box; margin: 0; padding: 0; }
  html, body {
    width: 1200px;
    height: 1200px;
    overflow: hidden;
    background: var(--page);
  }
  body {
    display: flex;
    flex-direction: column;
    align-items: center;
    justify-content: center;
    gap: 28px;
    font-family: "Carlito", "Calibri", sans-serif;
    color: var(--ink);
  }
  .card {
    position: relative;
    width: 960px;
    height: 558px;
    overflow: hidden;
    background:
      radial-gradient(ellipse 45% 35% at 88% 95%, rgba(139, 152, 192, 0.75) 0%, rgba(139, 152, 192, 0) 100%),
      radial-gradient(ellipse 70% 65% at 72% 58%, var(--mist) 0%, var(--steel) 32%, var(--navy) 62%, var(--navy-deep) 100%);
  }
  .emblem {
    position: absolute;
    left: 78px;
    top: 62px;
    width: 380px;
    height: 418px;
  }
  .card-title {
    position: absolute;
    left: 460px;
    width: 452px;
    top: 66px;
    text-align: center;
    font-weight: 700;
    font-size: 44px;
    line-height: 60px;
    letter-spacing: 0.3px;
    text-transform: uppercase;
  }
  .contact {
    position: absolute;
    left: 500px;
    width: 420px;
    top: 410px;
    text-align: center;
    font-size: 37px;
    line-height: 50px;
  }
  .contact-name { font-weight: 400; letter-spacing: 0.3px; }
  .contact-phone { font-style: italic; }
  .tagline {
    position: absolute;
    left: 0;
    right: 0;
    top: 170px;
    text-align: center;
    font-weight: 700;
    font-size: 51px;
    line-height: 68px;
    text-shadow: 0 6px 14px rgba(20, 28, 60, 0.35);
  }
  .email {
    position: absolute;
    left: 0;
    right: 0;
    top: 434px;
    text-align: center;
    font-style: italic;
    font-size: 34px;
  }
</style>
</head>
<body>
  <section class="card card-front">
    <svg class="emblem" viewBox="0 0 380 418" role="img" aria-label="White tree emblem with a child hugging a puppy beneath it">
      <defs>
        <radialGradient id="emblem-glow" cx="50%" cy="45%" r="60%">
          <stop offset="0%" stop-color="#ffffff" stop-opacity="0.95"/>
          <stop offset="100%" stop-color="#e6ecf4" stop-opacity="0.85"/>
        </radialGradient>
      </defs>
      <rect x="0" y="0" width="380" height="418" rx="40" fill="url(#emblem-glow)"/>
    </svg>
    <h1 class="card-title">Reiki for Kids<br>&amp; Creatures</h1>
    <div class="contact">
      <p class="contact-name">Maren Ellwood</p>
      <p class="contact-phone">0412 608 319</p>
    </div>
  </section>

  <section class="card card-back">
    <p class="tagline">Reiki - relaxes, restores balance<br>&amp; promotes healing</p>
    <p class="email">reikiforkidsandcreatures@mailbox.com</p>
  </section>
</body>
</html>
```